Brindle Works Australia Website

Brindle Works Australia (BWA) is a Industrial, Mining & Transport Services provider in Australia. We require a website that is both pc and mobile freindly. The website will be used to both present our company services and give us exposure in a crowded market. The main page of the website will have a snapshot of who BWA is and its from this page that the user can click to enter the area of interest ie. Industrial, Mining and Transport. A disticted logo can be used to indicate the area in question.<br/>Within the industrial, Mining and the Transport services pages will need list and description of services that are provided, current customer lists and news pages.<br/>The website will need a contacts page so prospective customers can get in contact with BWA.<br/>The website design will require a user freindly back end so future updates and ammendments can be carriedout by less experienced people within the BWA business.

Target Market(s)

Industrial, Mining and Transport Services provider markets

Coding

Number of Pages Required

5+ page

Font styles to use
Sans Serif

Colors
00a990

Requirements
Must have
• Ability to build servises with in services. because the main service area is only the main service with in each service group there is alot of smaller services / tasks.
• Key wording for easy seach engine capabilities. The website will need to be search engine freindly.

```html
<!DOCTYPE html>
<html lang="en">
<head>
<meta charset="utf-8">
<title>Brindle Works Australia – Mining and Transport Services</title>
<link href="https://fonts.googleapis.com/css2?family=Poppins:wght@300;400;500;600;700&display=swap" rel="stylesheet">
<style>
:root{
  --brand:#00a990;
  --ink:#111;
  --text:#555;
  --muted:#888;
  --line:#dcdcdc;
  --panel:#f3f3f3;
  --dark:#1c1c1c;
  --white:#fff;
}
*{box-sizing:border-box;margin:0;padding:0}
html,body{width:1200px;height:3525px;overflow:hidden;background:var(--white)}
body{font-family:'Poppins',sans-serif;color:var(--ink)}
.page{position:relative;width:1200px;height:3525px;overflow:hidden}
.abs{position:absolute}
.accent{color:var(--brand)}
/* header */
.site-header{left:0;top:0;width:1200px;height:62px;background:var(--white);box-shadow:0 1px 3px rgba(0,0,0,.08);z-index:5}
.brand{left:193px;top:9px;display:flex;align-items:center;gap:8px}
.brand-mark{width:12px;height:12px;background:var(--brand)}
.brand-name{font-weight:700;font-size:28px;color:#1d3b2a;line-height:1}
.brand-sub{font-size:8px;font-weight:600;color:#1d3b2a;line-height:1.2;letter-spacing:.3px}
.nav{top:23px;font-size:12px;color:#222}
.nav.active{color:var(--brand);border-bottom:1px solid var(--brand);padding-bottom:4px}
.btn-outline{border:1px solid var(--brand);color:var(--brand);font-size:12px;display:flex;align-items:center;justify-content:center}
/* hero */
.hero{left:0;top:62px;width:1200px;height:455px;background:linear-gradient(100deg,#3a2a1c 0%,#5a4128 45%,#7a5a34 70%,#4e3a24 100%)}
.hero-frame{left:193px;top:126px;width:100px;height:157px;border:4px solid var(--brand);border-right:none}
.hero-frame::after{content:"";position:absolute;right:0;top:-4px;width:0}
.hero-title{left:227px;top:148px;font-size:30px;font-weight:700;line-height:37px;color:var(--white)}
.hero-sub{left:300px;top:268px;font-size:12px;color:var(--white)}
.hero-btn{top:323px;height:31px;font-size:11px;display:flex;align-items:center;justify-content:center}
.hero-dots{left:193px;top:389px;display:flex;gap:7px}
.hero-dots span{width:14px;height:2px;background:var(--white)}
.hero-dots span.on{background:var(--brand)}
.machine{left:588px;top:130px;width:465px;height:434px;border-radius:40% 30% 20% 30%;background:radial-gradient(ellipse at 55% 55%,#f2b51c 0%,#d99a12 40%,rgba(40,30,20,.0) 72%)}
.scroll-mouse{left:591px;top:432px;width:16px;height:24px;border:2px solid var(--brand);border-radius:3px}
.scroll-mouse::after{content:"";position:absolute;left:5px;top:5px;width:2px;height:6px;background:var(--white)}
/* shared headings */
.ghost{left:0;width:1200px;text-align:center;font-size:36px;font-weight:700;color:var(--white);text-shadow:0 0 2px rgba(0,0,0,.35),0 0 1px rgba(0,0,0,.3)}
.section-title{left:0;width:1200px;text-align:center;font-size:31px;font-weight:700;color:var(--ink)}
/* about */
.rule{height:1px;background:var(--brand)}
.about-panel{left:193px;top:724px;width:531px;height:290px;background:var(--white);box-shadow:0 0 6px rgba(0,0,0,.15)}
.panel-head{height:37px;background:var(--brand);color:var(--white);font-size:15px;font-weight:500;display:flex;align-items:center;justify-content:space-between;padding:0 16px}
.about-photo{left:12px;top:56px;width:219px;height:217px;background:linear-gradient(160deg,#3b2c1e,#1a120b 60%,#6a4a1c)}
.about-copy{left:250px;top:56px;width:268px}
.about-copy h3{font-size:15px;font-weight:600;margin-bottom:14px}
.about-copy p{font-size:10.5px;line-height:17px;color:var(--text);font-weight:300}
.accordion{left:193px;top:1036px;width:531px;height:36px;background:var(--white);box-shadow:0 0 6px rgba(0,0,0,.15);display:flex;align-items:center;justify-content:space-between;padding:0 16px;font-size:15px;font-weight:500}
.quote{left:756px;top:724px;width:249px;height:348px;background:var(--panel)}
.quote-head{height:37px;background:var(--ink);color:var(--white);font-size:15px;font-weight:600;display:flex;align-items:center;justify-content:center}
.field{left:16px;width:217px;height:27px;background:var(--white);border:1px solid var(--line);font-size:9px;color:var(--muted);padding:8px 14px}
.submit{left:0;bottom:0;width:249px;height:36px;background:var(--brand);color:var(--white);font-size:15px;font-weight:600;display:flex;align-items:center;justify-content:center}
/* partners */
.partners{left:0;top:1135px;width:1200px;height:196px;background:linear-gradient(90deg,#1a1a24,#2b2633 50%,#3a3040)}
.partner-strip{left:194px;top:1185px;width:811px;height:86px;background:var(--white);display:flex;align-items:center;justify-content:space-around;padding:0 30px}
.badge{background:#dfe3e8}
.arrow-dot{top:1214px;width:28px;height:28px;border-radius:50%;background:var(--white);border:1px solid var(--line)}
/* services */
.intro{left:300px;width:600px;text-align:center;font-size:12px;line-height:21px;color:#333}
.card{background:var(--white);box-shadow:0 0 8px rgba(0,0,0,.12);padding:30px 12px}
.card h3{font-size:18px;font-weight:600;color:var(--brand);margin-bottom:16px}
.card p{font-size:9.5px;line-height:16px;color:var(--text)}
.card .more{position:absolute;left:12px;bottom:30px;font-size:13px;color:var(--brand)}
.card.featured{background:var(--brand)}
.card.featured h3,.card.featured p,.card.featured .more{color:var(--white)}
.card-icon{position:absolute;right:16px;bottom:24px}
/* testimonial */
.testimonial{left:0;top:2170px;width:1200px;height:303px;background:linear-gradient(180deg,#2a2e2a,#3c3a30 55%,#2a2824)}
.avatar{left:551px;top:2126px;width:98px;height:98px;border-radius:50%;background:linear-gradient(160deg,#e9e9e9,#b9b2a8);border:6px solid #d8d8d8}
.quote-text{left:295px;top:2318px;width:610px;text-align:center;font-size:11.5px;line-height:19px;color:var(--white)}
/* team */
.member{top:2674px;width:185px;height:219px}
.member .name{position:absolute;left:12px;bottom:22px;font-size:10px;color:var(--brand)}
.member .role{position:absolute;left:12px;bottom:8px;font-size:9px;color:var(--white)}
/* footer */
.footer{left:0;top:3023px;width:1200px;height:502px;background:linear-gradient(180deg,#232323,#2e2e2c 60%,#252525)}
.foot-col{top:3187px;width:190px}
.foot-col h4{font-size:15px;font-weight:500;color:var(--brand);margin-bottom:14px}
.foot-col li{list-style:none;font-size:10.5px;line-height:23px;color:var(--white)}
.foot-contact{display:flex;gap:12px;align-items:flex-start;font-size:10.5px;line-height:23px;color:var(--white);margin-bottom:18px}
.social{display:flex;gap:22px;margin-top:20px}
.social span{width:12px;height:12px;border-radius:50%;background:var(--white)}
.social span:first-child{background:var(--brand)}
.foot-base{top:3498px;font-size:10.5px;color:var(--white)}
</style>
</head>
<body>
<div class="page">

  <header class="abs site-header">
    <div class="abs brand">
      <span class="brand-mark"></span>
      <div>
        <div class="brand-name">BWA</div>
        <div class="brand-sub">BRINDLE WORKS AUSTRALIA<br>MINING AND TRANSPORT</div>
      </div>
    </div>
    <a class="abs nav active" style="left:513px">Home</a>
    <a class="abs nav" style="left:585px">About Us</a>
    <a class="abs nav" style="left:677px">Our Services</a>
    <a class="abs nav" style="left:789px">Contact Us</a>
    <a class="abs btn-outline" style="left:899px;top:19px;width:106px;height:25px">Get A Quote</a>
  </header>

  <section class="abs hero" aria-label="Hero"></section>
  <div class="abs hero-frame"></div>
  <h1 class="abs hero-title">Welcome to<br><span class="accent">Brindle Works</span><br>Australia <span class="accent">(BWA)</span></h1>
  <p class="abs hero-sub">Mining and Transport Services</p>
  <a class="abs hero-btn btn-outline" style="left:193px;width:124px">Explore Services</a>
  <a class="abs hero-btn" style="left:337px;width:98px;border:1px solid #fff;color:#fff">Contact Us</a>
  <div class="abs hero-dots"><span></span><span></span><span class="on"></span><span></span><span></span></div>
  <div class="abs machine" role="img" aria-label="Yellow backhoe loader with raised front bucket"></div>
  <div class="abs scroll-mouse"></div>

  <div class="abs ghost" style="top:598px">Few Words About Our Mission &amp; Vision</div>
  <h2 class="abs" style="left:193px;top:654px;font-size:30px;font-weight:700">Who <span class="accent">We</span> Are</h2>
  <div class="abs rule" style="left:393px;top:673px;width:363px"></div>
  <a class="abs btn-outline" style="left:756px;top:659px;width:111px;height:30px">Read More</a>
  <div class="abs rule" style="left:867px;top:673px;width:138px"></div>

  <div class="abs about-panel">
    <div class="panel-head"><span>About Us</span><span>—</span></div>
    <div class="abs about-photo" role="img" aria-label="Mining excavator lit up at night"></div>
    <div class="abs about-copy">
      <h3>What is BWA Australia?</h3>
      <p>Lorem Ipsum is simply dummy text of the printing and typesetting industry. Lorem Ipsum has been the industry's standard dummy text ever since the 1500s, when an unknown printer took a galley of type and scrambled it to make a type specimen book. It has survived not only five centuries, but also the leap into electronic typesetting, remaining essentially unchanged. It was popularised in the 1960s with the release of Letraset sheets containing Lorem Ipsum passages, and more recently with desktop publishing software like Aldus PageMaker.</p>
    </div>
  </div>
  <div class="abs accordion"><span>Our Mission and Vision</span><span style="font-size:22px;font-weight:300">+</span></div>

  <form class="abs quote">
    <div class="quote-head">Get A Free Quote</div>
    <div class="abs field" style="top:53px">Your Name</div>
    <div class="abs field" style="top:93px">Your Email Address</div>
    <div class="abs field" style="top:133px">Your Phone Number</div>
    <div class="abs field" style="top:173px">Quote Subject</div>
    <div class="abs field" style="top:212px;height:81px">Your Message</div>
    <div class="abs submit">Submit Now</div>
  </form>

  <section class="abs partners" role="img" aria-label="Steel structure silhouette at dusk"></section>
  <div class="abs partner-strip">
    <div class="badge" style="width:98px;height:36px;border-radius:3px"></div>
    <div class="badge" style="width:150px;height:22px"></div>
    <div class="badge" style="width:92px;height:38px;border-radius:4px"></div>
    <div class="badge" style="width:46px;height:46px;border-radius:50%"></div>
    <div class="badge" style="width:120px;height:24px"></div>
  </div>
  <div class="abs arrow-dot" style="left:180px"></div>
  <div class="abs arrow-dot" style="left:993px"></div>
  <svg class="abs" style="left:440px;top:1300px" width="320" height="32" viewBox="0 0 320 32">
    <path d="M0 32 C80 32 110 2 160 2 C210 2 240 32 320 32 Z" fill="#fff"/>
    <path d="M148 15 L160 25 L172 15" fill="none" stroke="#00a990" stroke-width="2"/>
  </svg>

  <div class="abs ghost" style="top:1376px">Some Of Our Services</div>
  <h2 class="abs section-title" style="top:1429px">Our <span class="accent">Services</span></h2>
  <p class="abs intro" style="top:1489px">It is a long established fact that a reader will be distracted by the readable content of a page when looking at its layout. The point of using Lorem Ipsum is that it has a more-or-less normal distribution of letters, as opposed to using 'Content here.</p>

  <article class="abs card" style="left:193px;top:1624px;width:243px;height:275px">
    <h3>Industrial Services</h3>
    <p>BWA Industrial Services Division offers an integrated site service and maintenance of your fixed plant. Our team are experienced in developing site-specific maintenance / service plans to ensure you critical site equipment stays operational. BWA field service units can deploy to your site 24/7 in the event of a breakdown to ensure you are back.</p>
    <span class="more">Read More →</span>
    <svg class="card-icon" width="34" height="36" viewBox="0 0 34 36"><path d="M3 34V18l9-6v6l9-6v6l9-6v22Z" fill="#111"/><rect x="6" y="2" width="4" height="12" fill="#111"/><rect x="20" y="2" width="4" height="10" fill="#111"/></svg>
  </article>
  <article class="abs card featured" style="left:460px;top:1594px;width:280px;height:335px;padding:58px 30px">
    <h3>Mining Services</h3>
    <p>BWA Mining Services Division offers an integrated service in equipment rental, maintenance and earthmoving. Supported by a modern and comprehensive fleet and experienced mechanical technicians that have previous OEM experience and an earthmoving team with experience in all aspects of civil and mining earthmoving.</p>
    <span class="more" style="left:30px;bottom:62px">Read More →</span>
    <svg class="card-icon" style="right:18px;bottom:54px" width="58" height="40" viewBox="0 0 58 40"><g fill="none" stroke="#fff" stroke-width="3"><rect x="4" y="22" width="34" height="14" rx="7"/><path d="M8 22V6h14l6 16M38 26l14-8 4 16"/></g></svg>
  </article>
  <article class="abs card" style="left:762px;top:1624px;width:243px;height:275px">
    <h3>Transport Services</h3>
    <p>BWA Transport Division specialises in the transportation of all types of materials such as, Steel, Structural Steel, Concrete Building Panels, Machinery, Palletised freight and bulk products, all of which are handled with the same amount of care and attention. Our fleet services Mining, Oil &amp; Gas and industrial clients across Western Australia. Our team..</p>
    <span class="more">Read More →</span>
    <svg class="card-icon" width="58" height="40" viewBox="0 0 58 40"><rect x="2" y="4" width="34" height="24" fill="#111"/><path d="M38 12h10l8 10v8H38Z" fill="#111"/><circle cx="14" cy="32" r="6" fill="#111" stroke="#fff" stroke-width="2"/><circle cx="46" cy="32" r="6" fill="#111" stroke="#fff" stroke-width="2"/></svg>
  </article>

  <div class="abs ghost" style="top:1988px">What Our Client Says</div>
  <h2 class="abs section-title" style="top:2041px">Our <span class="accent">Testimonials</span></h2>
  <section class="abs testimonial" role="img" aria-label="Mining site with conveyor machinery"></section>
  <div class="abs avatar" role="img" aria-label="Client portrait"></div>
  <div class="abs" style="left:0;width:1200px;top:2238px;text-align:center;font-size:14px;color:var(--brand)">Rory Calder</div>
  <div class="abs" style="left:0;width:1200px;top:2266px;text-align:center;font-size:11px;color:#fff">CEO Company Name</div>
  <p class="abs quote-text">It is a long established fact that a reader will be distracted by the readable content of a page when looking at its layout. The point of using Lorem Ipsum is that it has a more-or-less normal distribution of letters, as opposed to using 'Content here.</p>
  <div class="abs hero-dots" style="left:548px;top:2419px"><span></span><span></span><span class="on"></span><span></span><span></span></div>

  <div class="abs ghost" style="top:2535px">Meet Our Team</div>
  <h2 class="abs section-title" style="top:2588px">Our <span class="accent">Team</span></h2>
  <div class="abs member" style="left:202px;background:linear-gradient(180deg,#e8c24a,#c89a50 40%,#2a2a2a)" role="img" aria-label="Manager in yellow hard hat">
    <span class="name">Rory Calder</span><span class="role">Manager</span></div>
  <div class="abs member" style="left:406px;background:linear-gradient(180deg,#9aa0a8,#5a5f66 40%,#222)" role="img" aria-label="Worker in orange hard hat">
    <span class="name">Liam Porter</span><span class="role">Worker</span></div>
  <div class="abs member" style="left:609px;background:linear-gradient(180deg,#d9d4cc,#d97a2a 55%,#2a2a2a)" role="img" aria-label="Supervisor in hi-vis vest">
    <span class="name">Owen Marsh</span><span class="role">Supervisor</span></div>
  <div class="abs member" style="left:813px;background:linear-gradient(180deg,#a9b6c4,#e6a24a 55%,#2a2a2a)" role="img" aria-label="Worker in white hard hat">
    <span class="name">Evan Hollis</span><span class="role">Worker</span></div>
  <svg class="abs" style="left:566px;top:2930px" width="68" height="18" viewBox="0 0 68 18">
    <path d="M26 9H3M10 2L3 9l7 7" fill="none" stroke="#111" stroke-width="2"/>
    <path d="M42 9h23M58 2l7 7-7 7" fill="none" stroke="#00a990" stroke-width="2"/>
  </svg>

  <footer class="abs footer" role="img" aria-label="Industrial plant with silos, darkened"></footer>
  <h2 class="abs" style="left:193px;top:3085px;font-size:29px;font-weight:500;color:#fff">Quick Links</h2>
  <div class="abs rule" style="left:193px;top:3133px;width:188px"></div>

  <div class="abs foot-col" style="left:193px">
    <h4>Industrial Services</h4>
    <ul><li>• Field Services Units</li><li>• Onsite Breakdown Services</li><li>• Generator Rental</li><li>• Site Specific Preventive Maintenance Plans</li><li>• Plant Decommissioning and Relocation Services</li></ul>
  </div>
  <div class="abs foot-col" style="left:402px">
    <h4>Mining Services</h4>
    <ul><li>• Field Services Units</li><li>• Onsite Breakdown Services</li><li>• Onsite Mechanical Services</li><li>• Equipment Rental</li><li>• Civil &amp; Mining</li><li>• Generator Rental</li><li>• Fuel &amp; oil site tank storage solutions</li></ul>
  </div>
  <div class="abs foot-col" style="left:611px">
    <h4>Transport Services</h4>
    <ul><li>• Local deliveries in Perth metro area</li><li>• Linehaul to regional towns and even remote country sites</li><li>• Documentation Collection from your Agents</li><li>• Depots in Perth &amp; Karratha</li><li>• Bulk products Logistics (Liquids &amp; Solids)</li><li>• Trailer Rental Services</li></ul>
  </div>
  <div class="abs foot-col" style="left:821px;width:190px">
    <h4>Our Address</h4>
    <div class="foot-contact"><svg width="14" height="16" viewBox="0 0 14 16" style="margin-top:4px;flex:none"><path d="M7 15s5-5 5-9A5 5 0 0 0 2 6c0 4 5 9 5 9Z" fill="none" stroke="#fff" stroke-width="1.4"/><circle cx="7" cy="6" r="1.8" fill="#fff"/></svg><span>Unit 12, Ridge Road, Australia-600016</span></div>
    <div class="foot-contact"><svg width="14" height="12" viewBox="0 0 14 12" style="margin-top:6px;flex:none"><rect x="1" y="1" width="12" height="10" fill="none" stroke="#fff" stroke-width="1.2"/><path d="M1 1l6 5 6-5" fill="none" stroke="#fff" stroke-width="1.2"/></svg><span>info@brindleworks.example</span></div>
    <div class="foot-contact"><svg width="14" height="16" viewBox="0 0 14 16" style="margin-top:4px;flex:none"><rect x="3" y="1" width="8" height="14" rx="1.5" fill="none" stroke="#fff" stroke-width="1.4"/><circle cx="7" cy="12" r="1" fill="#fff"/></svg><span>+00-555-010-200</span></div>
    <div class="social" aria-label="Social links"><span></span><span></span><span></span></div>
  </div>

  <div class="abs" style="left:193px;top:3482px;width:812px;height:1px;background:rgba(255,255,255,.3)"></div>
  <a class="abs foot-base" style="left:193px">Privacy Policy</a>
  <a class="abs foot-base" style="left:303px">Contact Us</a>
  <p class="abs foot-base" style="right:195px">© 2020 <span class="accent">BWA Pvt. Ltd.</span> All Rights Reserved</p>
</div>
</body>
</html>
```